Skyreach Northern Flights
Private Charters
Skyreach Northern Flights  - Aviation
Creative Brief
Cutting-Edge
Tamara Holbrook
Business Development
5127 N. Darrow, Suite 240 Scottsdale, AZ 85254
tholbrook@skyreachnorthernflights.example
www.skyreachnorthernflights.example

```html
<!DOCTYPE html>
<html lang="en">
<head>
<meta charset="utf-8">
<title>Skyreach Northern Flights – Stationery</title>
<link rel="stylesheet" href="https://fonts.googleapis.com/css2?family=Cinzel:wght@400&family=Lato:wght@400;700&display=swap">
<style>
  :root {
    --backdrop: #b8b8b8;
    --paper: #ffffff;
    --maroon: #6e2a2c;
    --maroon-text: #7b3a3a;
    --card-grey: #6c6c66;
    --ink: #555555;
    --light-ink: #8a8a8a;
    --edge: #d9d9d9;
  }
  * { margin: 0; padding: 0; box-sizing: border-box; }
  html, body { width: 1200px; height: 684px; overflow: hidden; background: var(--backdrop); }
  .canvas { position: relative; width: 1200px; height: 684px; font-family: "Lato", sans-serif; color: var(--ink); }

  .sheet { position: absolute; background: var(--paper); box-shadow: 0 1px 3px rgba(0,0,0,.25); overflow: hidden; }

  .wordmark { font-family: "Cinzel", serif; font-weight: 400; color: var(--maroon-text); text-align: center; line-height: 1.2; letter-spacing: .04em; }
  .wordmark .mark { display: block; margin: 0 auto 6px; width: 14px; height: 14px; background: var(--maroon-text); }

  /* business card front */
  .card-front { left: 29px; top: 230px; width: 151px; height: 108px; background: var(--card-grey); display: flex; align-items: center; justify-content: center; }
  .card-front .wordmark { color: #ffffff; font-size: 11px; }
  .card-front .wordmark .mark { background: #ffffff; width: 12px; height: 12px; }

  /* business card back */
  .card-back { left: 29px; top: 343px; width: 151px; height: 108px; }
  .card-back .wordmark { position: absolute; left: 6px; top: 18px; width: 52px; font-size: 5.5px; }
  .card-back .wordmark .mark { width: 9px; height: 9px; margin-bottom: 3px; }
  .card-back .divider { position: absolute; left: 62px; top: 12px; width: 1px; height: 70px; background: var(--edge); }
  .card-back .person { position: absolute; left: 68px; top: 14px; }
  .card-back .person-name { font-family: "Cinzel", serif; font-size: 6.5px; color: var(--maroon-text); }
  .card-back .person-role { font-size: 4.5px; color: var(--light-ink); margin-top: 1px; }
  .card-back .contacts { position: absolute; left: 68px; top: 36px; list-style: none; font-size: 4px; line-height: 6.4px; color: var(--ink); }
  .card-back .contacts li::before { content: ""; display: inline-block; width: 3px; height: 3px; background: var(--maroon); margin-right: 3px; vertical-align: middle; }
  .card-back .band { position: absolute; left: 0; bottom: 0; width: 100%; height: 16px; background: var(--maroon); color: #fff; font-size: 4.5px; padding: 6px 8px; }

  /* letterhead */
  .letterhead { left: 187px; top: 34px; width: 430px; height: 628px; }
  .letterhead .wordmark { position: absolute; left: 44px; top: 40px; text-align: left; font-size: 15px; }
  .letterhead .wordmark .mark { margin: 0 0 8px 28px; width: 16px; height: 16px; }
  .letterhead .wordmark .sub { display: block; font-size: 8px; letter-spacing: .3em; padding-left: 36px; }
  .footer-line { position: absolute; left: 0; width: 100%; font-size: 5px; color: var(--ink); display: flex; gap: 14px; }
  .footer-line span::before { content: ""; display: inline-block; width: 4px; height: 4px; background: var(--maroon); margin-right: 3px; vertical-align: middle; }
  .letterhead .footer-line { bottom: 28px; padding: 0 44px; }
  .letterhead .web { position: absolute; left: 44px; bottom: 14px; font-size: 6px; color: var(--maroon-text); }
  .letterhead .band { position: absolute; left: 0; bottom: 0; width: 100%; height: 8px; background: var(--maroon); }

  /* envelope back with flap */
  .envelope-back { left: 641px; top: 62px; width: 530px; height: 257px; }
  .envelope-back svg { position: absolute; left: 0; top: 0; }
  .envelope-back .wordmark { position: absolute; left: 0; top: 46px; width: 100%; font-size: 17px; }
  .envelope-back .wordmark .sub { display: block; font-size: 8px; letter-spacing: .3em; }

  /* envelope front */
  .envelope-front { left: 641px; top: 365px; width: 530px; height: 254px; }
  .envelope-front .wordmark { position: absolute; left: 40px; top: 86px; font-size: 17px; text-align: left; }
  .envelope-front .wordmark .mark { margin: 0 0 8px 36px; width: 18px; height: 18px; }
  .envelope-front .wordmark .sub { display: block; font-size: 8px; letter-spacing: .3em; padding-left: 42px; }
  .envelope-front .footer-line { bottom: 32px; padding: 0 28px; gap: 18px; }
  .envelope-front .band { position: absolute; left: 0; bottom: 0; width: 100%; height: 24px; background: var(--maroon); color: #fff; font-size: 6px; padding: 9px 28px; }
</style>
</head>
<body>
<main class="canvas">

  <section class="sheet card-front">
    <div class="wordmark"><span class="mark"></span>Skyreach Northern<br>Flights</div>
  </section>

  <section class="sheet card-back">
    <div class="wordmark"><span class="mark"></span>Skyreach Northern Flights</div>
    <div class="divider"></div>
    <div class="person">
      <div class="person-name">Tamara Holbrook</div>
      <div class="person-role">Business Development</div>
    </div>
    <ul class="contacts">
      <li>(480) 555-0142</li>
      <li>(480) 555-0143</li>
      <li>(480) 555-0144</li>
      <li>tholbrook@skyreachnorthernflights.example</li>
      <li>5127 N. Darrow, Suite 240</li>
    </ul>
    <div class="band">www.skyreachnorthernflights.example</div>
  </section>

  <section class="sheet letterhead">
    <div class="wordmark"><span class="mark"></span>Skyreach Northern Flights<span class="sub">Charters</span></div>
    <div class="footer-line">
      <span>5127 N. Darrow, Suite 240 Scottsdale, AZ 85254</span>
      <span>(480) 555-0142</span>
      <span>(480) 555-0143</span>
      <span>tholbrook@skyreachnorthernflights.example</span>
    </div>
    <div class="web">www.skyreachnorthernflights.example</div>
    <div class="band"></div>
  </section>

  <section class="sheet envelope-back">
    <svg width="530" height="257" viewBox="0 0 530 257" aria-hidden="true">
      <path d="M0 0 L0 30 Q0 140 60 140 L470 140 Q530 140 530 30 L530 0" fill="none" stroke="#cfcfcf" stroke-width="1.2"/>
    </svg>
    <div class="wordmark">Skyreach Northern Flights<span class="sub">Charters</span></div>
  </section>

  <section class="sheet envelope-front">
    <div class="wordmark"><span class="mark"></span>Skyreach Northern Flights<span class="sub">Charters</span></div>
    <div class="footer-line">
      <span>5127 N. Darrow, Suite 240 Scottsdale, AZ 85254</span>
      <span>(480) 555-0142</span>
      <span>(480) 555-0143</span>
      <span>tholbrook@skyreachnorthernflights.example</span>
    </div>
    <div class="band">www.skyreachnorthernflights.example</div>
  </section>

</main>
</body>
</html>
```